Website design: Mobile Physiotherapy, Massage & Personal Training Business

I need a website that reflects a staff of health and fitness professionals. I would like the theme of the website to match the company logo (Summit Motion Wellness).
This is a link for a competitors website that I am fond of:
http://www.brackenrehab.com.au/
I am open to any and all creative and innovative designs.

```html
<!DOCTYPE html>
<html lang="en">
<head>
<meta charset="utf-8">
<title>Summit Motion Wellness</title>
<link rel="stylesheet" href="https://fonts.googleapis.com/css2?family=PT+Sans:ital,wght@0,400;0,700;1,700&family=Playfair+Display:ital,wght@1,700&display=swap">
<style>
:root{
  --red:#c4121a;
  --red-dark:#8d0a0f;
  --ink:#2d2d2d;
  --body:#3a3a3a;
  --night:#141414;
  --footer:#3b3b3b;
  --rule:#b7151b;
  --white:#ffffff;
}
*{margin:0;padding:0;box-sizing:border-box}
html,body{width:875px;height:1200px;overflow:hidden;background:var(--white)}
body{position:relative;font-family:"PT Sans",sans-serif;color:var(--body)}
.abs{position:absolute}

/* header */
.site-header{left:0;top:0;width:875px;height:112px;background:linear-gradient(180deg,#1c1a18,#0e0d0c)}
.logo-badge{left:126px;top:8px;width:188px;height:56px}
.logo-name{left:126px;top:8px;width:188px;height:56px;display:flex;align-items:center;justify-content:center;font-weight:700;font-size:15px;color:var(--red);text-align:center;line-height:1}
.social-tab{left:584px;top:0;width:128px;height:22px}
.social-dot{top:5px;width:12px;height:12px;border-radius:50%;background:#2a8fd6}
.hours-tab{left:472px;top:58px;width:252px;height:22px}
.hours-text{left:488px;top:62px;font-size:9px;color:#222;white-space:nowrap}
.hours-text a{color:var(--red);text-decoration:none}
.main-nav{left:126px;top:80px;width:602px;height:32px;background:linear-gradient(180deg,#d8141c,#9b0b10);display:flex;align-items:center;border-left:6px solid var(--red-dark)}
.main-nav a{color:var(--white);font-size:9px;text-decoration:none;text-transform:uppercase;height:32px;line-height:32px;padding:0 20px 0 28px}
.main-nav a.active{background:linear-gradient(180deg,#6b6b6b,#3e3e3e);padding:0 26px 0 26px;margin-left:2px}

/* hero */
.hero{left:0;top:112px;width:875px;height:358px;background:radial-gradient(ellipse at 30% 75%,#a53a14 0%,#5a2010 28%,#241612 55%,#121418 100%)}
.hero-people{left:432px;top:0;width:320px;height:358px;background:linear-gradient(160deg,#c98f6a,#8a5a3e 55%,#2b2f45)}
.hero-title{left:136px;top:88px;font-family:"Playfair Display",serif;font-style:italic;font-weight:700;font-size:42px;color:var(--white);letter-spacing:1px;text-transform:uppercase;line-height:1}
.hero-sub{left:136px;top:132px;font-family:"Playfair Display",serif;font-style:italic;font-weight:700;font-size:29px;color:var(--red);text-transform:uppercase;line-height:1}
.hero-copy{left:135px;top:164px;width:300px;font-size:8.4px;line-height:10.6px;color:var(--white);font-weight:700}

/* sections */
.section-title{font-size:24px;color:var(--ink);text-transform:uppercase;letter-spacing:.3px;line-height:1}
.service-photo{top:538px;width:170px;height:99px;border:1px solid #cfcfcf}
.service-title{top:654px;font-size:13px;text-transform:uppercase;color:var(--ink)}
.kicker{font-size:9px;color:var(--red)}
.small-copy{font-size:7.3px;line-height:9px;color:var(--body)}
.read-more{top:737px;width:56px;height:18px;background:linear-gradient(180deg,#c1141a,#870a0e);color:var(--white);font-size:7.5px;font-weight:700;line-height:18px;text-align:center}
.rule{left:147px;width:559px;height:2px;background:var(--rule)}
.date-box{top:846px;width:39px;height:44px;background:#2e2e2e;color:var(--white);text-align:center;font-size:8px;line-height:10px;padding-top:4px}
.date-box b{display:block;font-size:13px;line-height:14px}
.team-photo{top:1000px;width:78px;height:48px;border:1px solid #ddd}

/* footer */
.site-footer{left:0;top:1084px;width:875px;height:116px;background:var(--footer)}
.footer-badge{left:160px;top:1123px;width:108px;height:33px}
.footer-name{left:160px;top:1123px;width:108px;height:33px;display:flex;align-items:center;justify-content:center;font-weight:700;font-size:9px;color:var(--red)}
.copyright{left:169px;top:1159px;font-family:"Playfair Display",serif;font-style:italic;font-weight:700;font-size:9px;color:var(--white)}
.footer-links{left:486px;top:1128px;font-size:8.5px;color:var(--white);font-weight:700}
.footer-phone{left:489px;top:1148px;font-size:8.5px;color:var(--white);font-weight:700}
</style>
</head>
<body>

<header>
  <div class="abs site-header"></div>
  <svg class="abs logo-badge" viewBox="0 0 188 56">
    <line x1="30" y1="0" x2="20" y2="12" stroke="#aaa"/>
    <line x1="158" y1="0" x2="168" y2="12" stroke="#aaa"/>
    <polygon points="14,6 174,6 188,30 174,54 14,54 0,30" fill="#efefef" stroke="#9a9a9a"/>
    <circle cx="10" cy="30" r="2.5" fill="#333"/>
    <circle cx="178" cy="30" r="2.5" fill="#333"/>
  </svg>
  <div class="abs logo-name">Summit Motion<br>Wellness</div>

  <svg class="abs social-tab" viewBox="0 0 128 22"><polygon points="0,0 128,0 118,22 10,22" fill="#f2f2f2"/></svg>
  <span class="abs social-dot" style="left:608px"></span>
  <span class="abs social-dot" style="left:634px"></span>
  <span class="abs social-dot" style="left:660px;background:#1a6aa0"></span>
  <span class="abs social-dot" style="left:686px;background:#e8731a"></span>

  <svg class="abs hours-tab" viewBox="0 0 252 22"><polygon points="8,0 244,0 252,22 0,22" fill="#f2f2f2"/></svg>
  <div class="abs hours-text">Mon-Fri: 7.30am-7pm, Sat: 8am-2pm &nbsp;| <a href="#">Register</a> | &nbsp;<a href="#">Login</a></div>

  <nav class="abs main-nav">
    <a class="active" href="#">Home</a>
    <a href="#">About Us</a>
    <a href="#">Services</a>
    <a href="#">Products</a>
    <a href="#">Contacts</a>
  </nav>
</header>

<section class="abs hero">
  <div class="abs hero-people" role="img" aria-label="Fit man and woman holding dumbbells"></div>
  <h1 class="abs hero-title">Change Your</h1>
  <div class="abs hero-sub">Life Forever</div>
  <p class="abs hero-copy">Lorem ipsum dolor sit amet, consectetur adipiscing elit. Nulddg dfla eu mi varius, scelerisque sapien ac, tempodfr leo. Aenean eget pretium neque.t, consectetur adipiscing elit. Nulla eu mi varius, scelerisque sapien ac, tem-podfr leo. Aenean egling</p>
</section>

<h2 class="abs section-title" style="left:146px;top:494px">Our Services</h2>

<div class="abs service-photo" style="left:147px;background:linear-gradient(135deg,#7a8290,#c9b9a4)" role="img" aria-label="Physiotherapist stretching a patient's leg"></div>
<div class="abs service-photo" style="left:340px;background:linear-gradient(135deg,#e8e4df,#b9a69a)" role="img" aria-label="Group fitness class stretching on the floor"></div>
<div class="abs service-photo" style="left:535px;background:linear-gradient(135deg,#ffffff,#e6dccf)" role="img" aria-label="Smiling woman raising her arms"></div>

<h3 class="abs service-title" style="left:147px">Keeping You On Track</h3>
<h3 class="abs service-title" style="left:338px">Special Program</h3>
<h3 class="abs service-title" style="left:535px">Weight Loss Program</h3>
<div class="abs kicker" style="left:147px;top:672px">Morbi nibh lectus, ornare non porta</div>
<div class="abs kicker" style="left:338px;top:672px">Morbi nibh lectus, ornare non porta</div>
<div class="abs kicker" style="left:536px;top:672px">Morbi nibh lectus, ornare non porta</div>
<p class="abs small-copy" style="left:147px;top:686px;width:176px">Lorem ipsum dolor sit amet, consectetur adipiscing elit. Curabitur sodales a orci id pulvinar. Dsddffonec porta libero sem, quis faucibus erat ullamcorpefg r sodales.Curabitur sodales a orci id pulvinar.</p>
<p class="abs small-copy" style="left:338px;top:686px;width:176px">Lorem ipsum dolor sit amet, consectetur adipiscing elit. Curabitur sodales a orci id pulvinar. Dsddffonec porta libero sem, quis faucibus erat ullamcorpefg r sodales.Curabitur sodales a orci id pulvinar.</p>
<p class="abs small-copy" style="left:535px;top:686px;width:176px">Lorem ipsum dolor sit amet, consectetur adipiscing elit. Curabitur sodales a orci id pulvinar. Dsddffonec porta libero sem, quis faucibus erat ullamcorpefg r sodales.Curabitur sodales a orci id pulvinar.</p>
<a class="abs read-more" style="left:147px">Read More</a>
<a class="abs read-more" style="left:338px">Read More</a>
<a class="abs read-more" style="left:535px">Read More</a>

<div class="abs rule" style="top:774px"></div>

<h2 class="abs section-title" style="left:147px;top:803px">Recent News</h2>
<div class="abs date-box" style="left:145px"><b>23</b>Sep<br>2014</div>
<div class="abs date-box" style="left:341px"><b>23</b>Sep<br>2014</div>
<div class="abs date-box" style="left:537px"><b>23</b>Sep<br>2014</div>
<p class="abs small-copy" style="left:189px;top:846px;width:136px">Lorem ipsum dolor sit amet, consecte-tur adipiscing elit. Curabitur sodal essa orci id pulvinar. Dsddffonec porta lopt libero sem, quis faucibus erat ullamcor-pefg r sodales.</p>
<p class="abs small-copy" style="left:385px;top:846px;width:136px">Lorem ipsum dolor sit amet, consecte-tur adipiscing elit. Curabitur sodal essa orci id pulvinar. Dsddffonec porta lopt libero sem, quis faucibus erat ullamcor-pefg r sodales.</p>
<p class="abs small-copy" style="left:581px;top:846px;width:136px">Lorem ipsum dolor sit amet, consecte-tur adipiscing elit. Curabitur sodal essa orci id pulvinar. Dsddffonec porta lopt libero sem, quis faucibus erat ullamcor-pefg r sodales.</p>

<div class="abs rule" style="top:921px"></div>

<h2 class="abs section-title" style="left:148px;top:947px">About Our Team</h2>
<div class="abs kicker" style="left:151px;top:986px">Morbi nibh lectus, ornare</div>
<div class="abs kicker" style="left:350px;top:986px">Morbi nibh lectus, ornare</div>
<div class="abs kicker" style="left:549px;top:986px">Morbi nibh lectus, ornare</div>
<div class="abs team-photo" style="left:150px;background:linear-gradient(180deg,#e8e6e2,#3b8fd0)" role="img" aria-label="Team member portrait"></div>
<div class="abs team-photo" style="left:350px;background:linear-gradient(180deg,#4b4642,#b8342e)" role="img" aria-label="Team member portrait"></div>
<div class="abs team-photo" style="left:549px;background:linear-gradient(180deg,#ffffff,#e9c6b4)" role="img" aria-label="Team member portrait"></div>
<p class="abs small-copy" style="left:235px;top:1000px;width:86px">Lorem ipsum dolor sit amet, consec dfgrtetur adipi scsing elit. Curabi-tur sodalef essa orci id pulvinar.</p>
<p class="abs small-copy" style="left:435px;top:1000px;width:86px">Lorem ipsum dolor sit amet, consec dfgrtetur adipi scsing elit. Curabi-tur sodalef essa orci id pulvinar.</p>
<p class="abs small-copy" style="left:633px;top:1000px;width:86px">Lorem ipsum dolor sit amet, consec dfgrtetur adipi scsing elit. Curabi-tur sodalef essa orci id pulvinar.</p>

<footer>
  <div class="abs site-footer"></div>
  <div class="abs rule" style="top:1081px"></div>
  <svg class="abs footer-badge" viewBox="0 0 108 33">
    <polygon points="8,2 100,2 108,16.5 100,31 8,31 0,16.5" fill="#efefef" stroke="#9a9a9a"/>
  </svg>
  <div class="abs footer-name">Summit Motion Wellness</div>
  <div class="abs copyright">2014 © Privacy Policy</div>
  <div class="abs footer-links">HOME | ABOUT US | SERVICES | PRODUCTS | CONTACTS</div>
  <div class="abs footer-phone">Get In Touch With Us :1 800 555 01 234</div>
</footer>

</body>
</html>
```